Martial art rank diploma

Need a diploma for a martial arts belt rank . The art is Japanese in origin , traditional is good , stylish , eye catching .
Dragons are good , no cartoon figures . Tacky is not good . Something proud to display
No martial art poses
Must have place for date , head instructor signature

And must say (a blank for students name )
"Having confirmed with all standards and requirements set forth by Brantwell Martial Arts and Fitness , is hereby promoted to the rank of " ( a blank for the rank)
Updates

Reason: nice designs, need to see more to compare

Industry/Entity Type

Martial Art

Requirements
Must have
• Logo attached and name of the school
Nice to have
• Dragon , that does not look like a centipede .

maybe best to have a dragon in the background as a water mark type of thing.
Should not have
• Tacky look or cartoon figures, or any martial art poses

```html
<!DOCTYPE html>
<html lang="en">
<head>
<meta charset="utf-8">
<title>Certificate of Rank – Brantwell Martial Arts and Fitness</title>
<link href="https://fonts.googleapis.com/css2?family=Montserrat:ital,wght@0,300;0,400;0,500;0,700;0,800;0,900;1,400&display=swap" rel="stylesheet">
<style>
  :root {
    --ink: #434c53;
    --ink-dark: #111416;
    --accent: #f3400f;
    --accent-soft: #fbd7cb;
    --paper: #ffffff;
    --body-font: "Montserrat", Arial, sans-serif;
  }
  html, body {
    margin: 0;
    padding: 0;
    width: 1200px;
    height: 927px;
    overflow: hidden;
    background: var(--paper);
  }
  .certificate {
    position: relative;
    width: 1200px;
    height: 927px;
    font-family: var(--body-font);
    color: var(--ink);
  }
  .frame, .watermark {
    position: absolute;
    left: 0;
    top: 0;
  }
  .school-mark {
    position: absolute;
    left: 272px;
    top: 40px;
    width: 584px;
    height: 160px;
    display: flex;
    align-items: center;
    gap: 22px;
  }
  .school-mark__dot {
    width: 130px;
    height: 130px;
    border-radius: 50%;
    background: var(--ink);
    flex: none;
  }
  .school-mark__name {
    margin: 0;
    font-weight: 800;
    color: var(--ink);
    line-height: 1;
  }
  .school-mark__name .primary {
    display: block;
    font-size: 60px;
    letter-spacing: -1px;
  }
  .school-mark__name .secondary {
    display: block;
    font-size: 29px;
    margin-top: 8px;
  }
  .title {
    position: absolute;
    top: 235px;
    left: 0;
    width: 1200px;
    text-align: center;
    margin: 0;
    font-size: 37px;
    font-weight: 800;
    letter-spacing: 9px;
    color: var(--accent);
    line-height: 44px;
  }
  .line-text {
    position: absolute;
    left: 0;
    width: 1200px;
    text-align: center;
    margin: 0;
  }
  .lead {
    top: 336px;
    font-size: 30px;
    font-weight: 400;
    letter-spacing: 3.5px;
  }
  .student-name {
    top: 414px;
    font-size: 32px;
    font-weight: 900;
    letter-spacing: 5px;
    color: var(--ink-dark);
  }
  .promotion {
    top: 500px;
    font-size: 25px;
    font-weight: 300;
    letter-spacing: 2.5px;
  }
  .rank {
    top: 563px;
    font-size: 31px;
    font-weight: 900;
    letter-spacing: 5.5px;
    color: var(--ink-dark);
  }
  .date-row {
    position: absolute;
    top: 0;
    left: 0;
    margin: 0;
    width: 1200px;
    height: 0;
  }
  .date-row > span {
    position: absolute;
    white-space: nowrap;
    line-height: 32px;
  }
  .date-row .label {
    top: 647px;
    font-size: 24px;
    font-weight: 300;
    letter-spacing: 1.5px;
  }
  .date-row .label--on { left: 274px; }
  .date-row .label--of { left: 512px; }
  .date-row .fill {
    top: 645px;
    font-size: 28px;
    font-weight: 500;
    letter-spacing: 1.5px;
    color: var(--ink-dark);
    text-align: center;
  }
  .date-row .fill--day { left: 388px; width: 115px; }
  .date-row .fill--month { left: 615px; width: 315px; }
  .signature {
    position: absolute;
    top: 815px;
    left: 0;
    width: 1200px;
    text-align: center;
  }
  .signature__name {
    margin: 0;
    font-size: 26px;
    font-weight: 700;
    color: var(--accent);
    line-height: 32px;
  }
  .signature__role {
    margin: 0;
    font-size: 20px;
    font-style: italic;
    color: var(--ink);
    line-height: 24px;
  }
</style>
</head>
<body>
<main class="certificate">
  <svg class="frame" width="1200" height="927" viewBox="0 0 1200 927" aria-hidden="true">
    <rect x="35" y="103" width="224" height="20" fill="var(--accent)"/>
    <rect x="862" y="103" width="306" height="20" fill="var(--accent)"/>
    <g stroke="var(--ink)" stroke-width="7" fill="none">
      <polyline points="258,134 41,134 41,888 1162,888 1162,134 862,134"/>
    </g>
    <rect x="41" y="255" width="218" height="6" fill="var(--ink)"/>
    <rect x="935" y="255" width="227" height="6" fill="var(--ink)"/>
    <g fill="var(--accent-soft)">
      <circle cx="141" cy="188" r="37"/>
      <circle cx="1040" cy="188" r="37"/>
      <circle cx="80" cy="844" r="27"/>
      <circle cx="1121" cy="844" r="27"/>
    </g>
    <g fill="var(--ink)">
      <rect x="282" y="454" width="638" height="3"/>
      <rect x="315" y="601" width="574" height="3"/>
      <rect x="388" y="678" width="115" height="3"/>
      <rect x="615" y="678" width="315" height="3"/>
      <rect x="423" y="807" width="357" height="3"/>
    </g>
  </svg>

  <svg class="watermark" width="1200" height="927" viewBox="0 0 1200 927" role="img" aria-label="Faint dragon watermark behind the certificate text">
    <defs>
      <radialGradient id="watermarkTone" cx="50%" cy="50%" r="50%">
        <stop offset="0%" stop-color="#fbd7cb" stop-opacity="0.75"/>
        <stop offset="100%" stop-color="#fbd7cb" stop-opacity="0.15"/>
      </radialGradient>
    </defs>
    <ellipse cx="620" cy="555" rx="240" ry="235" fill="url(#watermarkTone)"/>
  </svg>

  <header class="school-mark">
    <span class="school-mark__dot" aria-hidden="true"></span>
    <h1 class="school-mark__name">
      <span class="primary">BRANTWELL</span>
      <span class="secondary">Martial Arts and Fitness</span>
    </h1>
  </header>

  <h2 class="title">CERTIFICATE OF RANK</h2>

  <p class="line-text lead">THIS DOCUMENT CERTIFIES THAT</p>
  <p class="line-text student-name">DANIEL HARROW</p>
  <p class="line-text promotion">has been promoted to the rank of</p>
  <p class="line-text rank">SENIOR RED BELT</p>

  <p class="date-row">
    <span class="label label--on">On this</span>
    <span class="fill fill--day">16th</span>
    <span class="label label--of">day of</span>
    <span class="fill fill--month">December 2013</span>
  </p>

  <footer class="signature">
    <p class="signature__name">Sensei Brantwell</p>
    <p class="signature__role">Chief Instructor</p>
  </footer>
</main>
</body>
</html>
```